Corporate Branding for Professional Services Company

This project is logo design, business card deisgn and letterhead design.

My client is a company name called Brightmere Staffing Ireland and they are a professional services company that provide the following services:

- Field Sales
- Merchandising
- Promotional Events & Demo's
- Sales Training
- Mystery Shopper
- POS placement & Mangement
- Field Marketing

Their target market is high end corporate companies so the logo, letterhead and business card will need to be very professional corporate looking. The idea that I pitched to them was that they are provision "Vision" to their clients, so how about putting a lighthouse in the logo with the name, possibly the lighthouse emitting a light trail also? Its an idea, play with it!

The colours are black with another complementing colour of your choice, definitely no pinks!

I need this designs done asap please.

Target Market(s)

Corporate Businesses, Professinoal Services company

Industry/Entity Type

Business Consultant

Font styles to use
Serif
Sans Serif

Requirements
Must have
• Professorial corporate Classy look and feel to it. Dark colours.
Should not have
• No Pink

```html
<!DOCTYPE html>
<html lang="en">
<head>
<meta charset="utf-8">
<title>Brightmere Staffing Ireland – Stationery</title>
<link rel="stylesheet" href="https://fonts.googleapis.com/css2?family=Cinzel:wght@400;600&family=Lato:wght@400&display=swap">
<style>
  :root {
    --ink-grey: #6b6c6f;
    --dark-grey: #58595b;
    --beam-yellow: #eeea5e;
    --pale-yellow: #f7f5b8;
    --paper: #ffffff;
    --shadow: rgba(0, 0, 0, 0.28);
  }
  * { margin: 0; padding: 0; box-sizing: border-box; }
  html, body {
    width: 779px; height: 1200px; overflow: hidden;
    background: var(--paper);
  }
  .canvas { position: relative; width: 779px; height: 1200px; }

  .brand-lockup {
    position: absolute; left: 0; width: 100%;
    display: flex; align-items: center; justify-content: center; gap: 12px;
  }
  .brand-dot { border-radius: 50%; background: var(--ink-grey); flex: none; }
  .brand-name {
    font-family: "Cinzel", serif; font-weight: 400; color: var(--ink-grey);
    letter-spacing: 0.04em; text-align: center; line-height: 1.15;
  }

  .main-logo { top: 120px; }
  .main-logo .brand-dot { width: 34px; height: 34px; }
  .main-logo .brand-name { font-size: 30px; }

  .card {
    position: absolute; top: 229px; height: 106px; background: var(--paper);
    box-shadow: 2px 3px 6px var(--shadow); overflow: hidden;
  }
  .card-front { left: 239px; width: 164px; text-align: center; }
  .card-back { left: 416px; width: 228px; }

  .card-front .brand-lockup { top: 8px; gap: 4px; }
  .card-front .brand-dot { width: 9px; height: 9px; }
  .card-front .brand-name { font-size: 6.5px; }
  .card-person {
    position: absolute; top: 32px; width: 100%;
    font-family: "Cinzel", serif; color: var(--ink-grey);
  }
  .card-person .person-name { font-size: 10px; letter-spacing: 0.05em; }
  .card-person .person-role { font-size: 6px; letter-spacing: 0.1em; margin-top: 1px; }
  .card-person .person-phone { font-family: "Lato", sans-serif; font-size: 5px; margin-top: 5px; }
  .card-contact {
    position: absolute; left: 18px; bottom: 16px; text-align: left;
    font-family: "Lato", sans-serif; font-size: 4.5px; color: var(--ink-grey); line-height: 1.5;
  }

  .service-list {
    position: absolute; left: 14px; top: 16px; list-style: none;
    font-family: "Cinzel", serif; font-size: 5.5px; color: var(--ink-grey); line-height: 1.7;
    letter-spacing: 0.04em;
  }
  .card-back .back-mark {
    position: absolute; right: 26px; top: 14px; width: 60px; height: 60px;
    border-radius: 50%; background: var(--pale-yellow);
  }

  .letterhead {
    position: absolute; left: 130px; top: 372px; width: 541px; height: 773px;
    background: var(--paper); box-shadow: 3px 4px 9px var(--shadow); overflow: hidden;
  }
  .letterhead-shapes { position: absolute; inset: 0; }
  .letterhead-sender {
    position: absolute; right: 22px; top: 10px; text-align: right;
    font-family: "Cinzel", serif; color: #fff;
  }
  .letterhead-sender .person-name { font-size: 17px; letter-spacing: 0.05em; }
  .letterhead-sender .person-role { font-size: 10px; letter-spacing: 0.12em; }
  .letterhead-sender .person-phone { font-family: "Lato", sans-serif; font-size: 8px; margin-top: 10px; }

  .letterhead .faint-logo { top: 385px; opacity: 0.35; gap: 8px; }
  .letterhead .faint-logo .brand-dot { width: 26px; height: 26px; }
  .letterhead .faint-logo .brand-name { font-size: 23px; }

  .letterhead-footer {
    position: absolute; left: 14px; bottom: 12px;
    font-family: "Lato", sans-serif; font-size: 6px; color: var(--dark-grey); line-height: 1.6;
    letter-spacing: 0.03em;
  }
</style>
</head>
<body>
<main class="canvas">

  <header class="brand-lockup main-logo">
    <span class="brand-dot"></span>
    <span class="brand-name">Brightmere Staffing Ireland</span>
  </header>

  <section class="card card-front">
    <div class="brand-lockup">
      <span class="brand-dot"></span>
      <span class="brand-name">Brightmere Staffing Ireland</span>
    </div>
    <div class="card-person">
      <p class="person-name">AOIFE BRENNAN</p>
      <p class="person-role">DIRECTOR</p>
      <p class="person-phone">086 555 0142</p>
    </div>
    <div class="card-contact">
      <p>aoife@brightmerestaffing.ie</p>
      <p>www.brightmerestaffing.ie</p>
    </div>
  </section>

  <section class="card card-back">
    <ul class="service-list">
      <li>Field Sales</li>
      <li>Merchandising</li>
      <li>Promotional Events &amp; Demo's</li>
      <li>Sales Training</li>
      <li>Mystery Shopper</li>
      <li>POS Placement &amp; Management</li>
      <li>Field Marketing</li>
    </ul>
    <span class="back-mark"></span>
  </section>

  <section class="letterhead">
    <svg class="letterhead-shapes" width="541" height="773" viewBox="0 0 541 773">
      <path d="M120 0 C250 10 420 45 541 100 L541 0 Z" fill="var(--dark-grey)"/>
      <path d="M0 590 C90 690 260 760 470 773 L0 773 Z" fill="var(--beam-yellow)"/>
      <path d="M0 620 C110 700 250 745 400 773 L0 773 Z" fill="#f4f18a"/>
    </svg>
    <div class="letterhead-sender">
      <p class="person-name">AOIFE BRENNAN</p>
      <p class="person-role">DIRECTOR</p>
      <p class="person-phone">086 555 0142</p>
    </div>
    <div class="brand-lockup faint-logo">
      <span class="brand-dot"></span>
      <span class="brand-name">Brightmere Staffing Ireland</span>
    </div>
    <footer class="letterhead-footer">
      <p>aoife@brightmerestaffing.ie</p>
      <p>www.brightmerestaffing.ie</p>
      <p>Unit 12 Harbour Business Park, Ardee, Co. Louth, Ireland</p>
    </footer>
  </section>

</main>
</body>
</html>
```